Window Cleaning Leaflet

Hi everyone,

I need a leaflet (couldn't find 'leaflet' as an option when begining this project - so one sided only) to send out to coastal properties in South side Melbourne. The Flyer is aimed at high net individuals, mummies, business people etc who own these properties who don't have time to clean the windows themselves (often multiple levels) and want their home looking fabulous in time for Christmas and NY's celebrations.

I would really love a new and original design for a window washing leaflet. something outside of the norm that 'pops' and makes people feel happy when they look at it.

I guess a point of differentiation is that I'm a female working in a mans industry so appeal to mothers looking for someone who is 'reliable, trustworthy and understanding of peoples needs'.

I have made an outline of what I would like included in the leaflet, so if you could please take a look, feel free to change things around, wording and layout etc. If you can make it sound more professional please do so.

I would like the colours to be 'happy' colours, maybe with a silly season theme?

Overall aesthetically pleasing is a must, I find most window cleaning leaflets fairly mundane and boring, please feel free to think outside the box. The more original the better.

Target Market(s)

People who own large Melbourne homes in affluent suburbs, mainly suburbs with a lot of large coastal properties. Generally owned by high net worth individuals who just don't have tme to clean the windows themselves due to their profession or hectic lifestyles but can afford to pay someone else to do it.

Industry/Entity Type

Window Cleaning

Requirements
Must have
• 1) The name of the business - Tilda’s Glass Gleaming Services
• 2) The coupon special and all details attached:
• Small Homes (up to 12 windows) $120
• Medium Homes (up to 16 windows) $180
• Large Homes (up to 20 windows, 2 storeys) $240
• 20% discount
• *Discount applicable to first time customers only.
• *All services include fly screen, sill and tracks cleaned as well as cobweb removal.
• *Houses with more than 20 windows (or two levels) will have an immediate quote provided upon inspection of the property with 20% discount applied.
• *Tilda’s Glass Gleaming Services are fully insured.
• 3) My contact number - 0418 263 591

```html
<!DOCTYPE html>
<html lang="en">
<head>
<meta charset="utf-8">
<title>Tilda’s Glass Gleaming Services – Leaflet</title>
<link rel="stylesheet" href="https://fonts.googleapis.com/css2?family=Alegreya:ital,wght@0,400;1,400;1,700&family=Dosis:wght@500;700&display=swap">
<style>
  :root {
    --ink: #141414;
    --cream: #fbf3d6;
    --cream-light: #fffaea;
    --hero-top: #8fb6df;
    --hero-bottom: #d9e6f2;
    --white: #ffffff;
  }
  * { margin: 0; padding: 0; box-sizing: border-box; }
  html, body { width: 900px; height: 1200px; overflow: hidden; background: #ffffff; }
  .leaflet {
    position: relative;
    width: 900px;
    height: 1200px;
    overflow: hidden;
    background: linear-gradient(180deg, var(--cream-light), var(--cream));
    font-family: "Dosis", sans-serif;
    color: var(--ink);
  }
  .hero { position: absolute; left: 0; top: 0; width: 900px; height: 540px; display: block; }
  .tagline {
    position: absolute;
    left: 520px;
    top: 40px;
    width: 310px;
    text-align: center;
    font-family: "Alegreya", serif;
    font-style: italic;
    font-weight: 700;
    font-size: 92px;
    line-height: 128px;
    color: var(--white);
    text-shadow: 2px 3px 4px rgba(0,0,0,0.75);
  }
  .brand { position: absolute; left: 0; top: 530px; width: 100%; text-align: center; font-family: "Alegreya", serif; font-style: italic; font-weight: 400; }
  .brand-name { font-size: 80px; line-height: 96px; font-weight: 400; }
  .brand-service { font-size: 56px; line-height: 66px; }
  .intro { position: absolute; left: 0; top: 705px; width: 100%; text-align: center; font-size: 20px; font-weight: 500; line-height: 25px; }
  .intro p + p { margin-top: 25px; }
  .phone { position: absolute; left: 0; top: 902px; width: 100%; text-align: center; font-size: 33px; font-weight: 700; letter-spacing: 0.5px; }
  .prices { position: absolute; left: 0; top: 966px; width: 100%; text-align: center; list-style: none; font-size: 23px; font-weight: 700; line-height: 33px; }
  .fine-print { position: absolute; left: 52px; top: 1084px; width: 800px; list-style: none; font-size: 13.5px; font-weight: 500; line-height: 18px; }
</style>
</head>
<body>
<main class="leaflet">
  <svg class="hero" viewBox="0 0 900 540" role="img" aria-label="Photo of a bright bedroom with large windows looking out over a lawn and mountains">
    <defs>
      <linearGradient id="heroFill" x1="0" y1="0" x2="0" y2="1">
        <stop offset="0" stop-color="var(--hero-top)"/>
        <stop offset="1" stop-color="var(--hero-bottom)"/>
      </linearGradient>
    </defs>
    <path d="M0 0 H900 V520 C700 470 420 520 0 545 Z" fill="url(#heroFill)"/>
  </svg>

  <p class="tagline">enjoy<br>the<br>view!</p>

  <header class="brand">
    <h1 class="brand-name">Tilda’s</h1>
    <p class="brand-service">Glass Gleaming Services</p>
  </header>

  <section class="intro">
    <p>Do you need your windows cleaned?<br>
    Are you simply too busy as a hard working parent to do it yourself?<br>
    Tilda understands and wants to help you - enjoy your home looking it’s best before<br>
    Christmas and NY’s celebrations begin.</p>
    <p>We provide a reliable, professional service, ensuring that your home will sparkle.<br>
    Call Tilda today and take advantage of our special introductory offer.</p>
  </section>

  <p class="phone">Tilda - 0418 263 591</p>

  <ul class="prices">
    <li>Small Homes (up to 12 windows) $120</li>
    <li>Medium Homes (up to 16 windows) $180</li>
    <li>Large Homes (up to 20 windows, 2 storeys) $240</li>
  </ul>

  <ul class="fine-print">
    <li>*Discount applicable to first time customers only.</li>
    <li>*All services include fly screen, sill and tracks cleaned as well as cobweb removal.</li>
    <li>*Houses with more than 20 windows (or two levels) will have an immediate quote provided upon inspection of the property with 20% discount applied.</li>
    <li>*Tilda’s Glass Gleaming Services are fully insured.</li>
  </ul>
</main>
</body>
</html>
```